Verdant Loop Advisors, LLC

I am looking for a simple, clear layout with my logo prominent and embossed, on the best quality card stock available. I would like the business name and phone number included on the card as well......I dont want my name anywhere on the card and I would like my logo embossed on the card......something simple with a white back......open to designs as long as they go along with recycling symbols and green type stuff.....The address, website, cell number, fax number, and email are listed below

5374 Tillbury Fenwood Road
Fenwick Hollow, MD 20999

c. 240.555.0143 f. 240.555.0187
e. sales@verdantloopadvisors.example
w. www.verdantloopadvisors.example

Industry/Entity Type

Recycling

```html
<!DOCTYPE html>
<html lang="en">
<head>
<meta charset="utf-8">
<title>Verdant Loop Advisors, LLC — Business Card Set</title>
<link href="https://fonts.googleapis.com/css2?family=Inter:wght@400;700&display=swap" rel="stylesheet">
<style>
  :root {
    --board-center: #a9a9a9;
    --board-edge: #6f6f6f;
    --card-white: #ffffff;
    --brand-green: #1d5a35;
    --brand-green-deep: #0f4d29;
    --brand-green-light: #3d6e4e;
    --ink-dark: #2b2522;
    --ink-body: #333333;
    --ink-on-green: #ffffff;
    --card-shadow: 0 2px 5px rgba(0,0,0,.35);
  }
  * { margin: 0; padding: 0; box-sizing: border-box; }
  html, body { width: 1200px; height: 1200px; overflow: hidden; }
  body {
    font-family: "Inter", Arial, sans-serif;
    background: radial-gradient(circle at 50% 50%, var(--board-center) 0%, var(--board-edge) 75%);
    position: relative;
  }
  .card {
    position: absolute;
    width: 353px;
    height: 202px;
    background: var(--card-white);
    box-shadow: var(--card-shadow);
    overflow: hidden;
  }
  .card--green {
    background: radial-gradient(circle at 40% 0%, var(--brand-green-light) 0%, var(--brand-green) 45%, var(--brand-green-deep) 100%);
    color: var(--ink-on-green);
  }
  .col-left { left: 234px; }
  .col-right { left: 603px; }
  .row-1 { top: 197px; }
  .row-2 { top: 497px; }
  .row-3 { top: 790px; }

  .wordmark {
    position: absolute;
    display: flex;
    align-items: center;
    gap: 8px;
    font-weight: 700;
    font-size: 16px;
    letter-spacing: .2px;
    color: var(--ink-dark);
    white-space: nowrap;
  }
  .wordmark__dot {
    width: 24px; height: 24px;
    border-radius: 50%;
    background: var(--brand-green);
    flex: none;
  }
  .front .wordmark { left: 50%; top: 50%; transform: translate(-50%, -50%); }

  .emblem {
    position: absolute;
    border-radius: 50%;
  }
  .emblem--green { background: var(--brand-green); }
  .emblem--white { background: var(--card-white); }

  .contact {
    position: absolute;
    font-size: 8px;
    line-height: 11.5px;
    color: var(--ink-body);
    white-space: nowrap;
  }
  .card--green .contact { color: var(--ink-on-green); }
  .contact--right { right: 22px; text-align: right; }
  .contact__group { margin-bottom: 7px; }
  .contact__line { display: flex; align-items: center; justify-content: flex-end; gap: 8px; }
  .contact__line .icon { order: 2; }
  .contact--left-icons .contact__line { justify-content: flex-start; }
  .contact--left-icons .contact__line .icon { order: 0; }
  .icon { width: 7px; height: 7px; flex: none; fill: currentColor; }
  .card--white .contact--right .icon { fill: var(--brand-green); }
  .contact--left-icons .icon { fill: #555; }
  .icon-spacer { width: 7px; flex: none; }
</style>
</head>
<body>
<svg width="0" height="0" style="position:absolute">
  <symbol id="i-home" viewBox="0 0 10 10"><path d="M5 1 1 5h1.5v4h2V6.5h1V9h2V5H9z"/></symbol>
  <symbol id="i-phone" viewBox="0 0 10 10"><path d="M2.2 1 3.8 2.8 3 4a5 5 0 0 0 3 3l1.2-.8L9 7.8 8 9C4.5 9 1 5.5 1 2z"/></symbol>
  <symbol id="i-fax" viewBox="0 0 10 10"><path d="M3 1h4v3H3zM1 5h8v4H1z"/></symbol>
  <symbol id="i-mail" viewBox="0 0 10 10"><path d="M1 2h8v6H1zm1 1v.4l3 2 3-2V3L5 5z"/></symbol>
  <symbol id="i-web" viewBox="0 0 10 10"><circle cx="5" cy="5" r="4"/></symbol>
</svg>

<section class="card card--white front col-left row-1">
  <div class="wordmark"><span class="wordmark__dot"></span>Verdant Loop Advisors, LLC</div>
</section>
<section class="card card--white col-right row-1">
  <div class="emblem emblem--green" style="left:26px;top:22px;width:98px;height:98px;"></div>
  <div class="contact contact--right" style="top:99px;">
    <div class="contact__group">
      <div class="contact__line"><svg class="icon"><use href="#i-home"/></svg>5374 Tillbury Fenwood Road</div>
      <div class="contact__line"><span class="icon-spacer"></span>Fenwick Hollow, MD 20999</div>
    </div>
    <div class="contact__group">
      <div class="contact__line"><svg class="icon"><use href="#i-phone"/></svg>240.555.0143</div>
      <div class="contact__line"><svg class="icon"><use href="#i-fax"/></svg>240.555.0187</div>
    </div>
    <div class="contact__group">
      <div class="contact__line"><svg class="icon"><use href="#i-mail"/></svg>sales@verdantloopadvisors.example</div>
      <div class="contact__line"><svg class="icon"><use href="#i-web"/></svg>www.verdantloopadvisors.example</div>
    </div>
  </div>
</section>

<section class="card card--white front col-left row-2">
  <div class="wordmark"><span class="wordmark__dot"></span>Verdant Loop Advisors, LLC</div>
</section>
<section class="card card--green col-right row-2">
  <div class="emblem emblem--white" style="left:26px;top:53px;width:96px;height:96px;"></div>
  <div class="contact contact--right" style="top:60px;">
    <div class="contact__group">
      <div class="contact__line"><svg class="icon"><use href="#i-home"/></svg>5374 Tillbury Fenwood Road</div>
      <div class="contact__line"><span class="icon-spacer"></span>Fenwick Hollow, MD 20999</div>
    </div>
    <div class="contact__group">
      <div class="contact__line"><svg class="icon"><use href="#i-phone"/></svg>240.555.0143</div>
      <div class="contact__line"><svg class="icon"><use href="#i-fax"/></svg>240.555.0187</div>
    </div>
    <div class="contact__group">
      <div class="contact__line"><svg class="icon"><use href="#i-mail"/></svg>sales@verdantloopadvisors.example</div>
      <div class="contact__line"><svg class="icon"><use href="#i-web"/></svg>www.verdantloopadvisors.example</div>
    </div>
  </div>
</section>

<section class="card card--green col-left row-3">
  <div class="emblem emblem--white" style="left:124px;top:49px;width:104px;height:104px;"></div>
</section>
<section class="card card--white col-right row-3">
  <div class="wordmark" style="left:64px;top:38px;"><span class="wordmark__dot"></span>Verdant Loop Advisors, LLC</div>
  <div class="contact contact--left-icons" style="left:30px;top:138px;">
    <div class="contact__line"><svg class="icon"><use href="#i-home"/></svg>5374 Tillbury Fenwood Road</div>
    <div class="contact__line"><span class="icon-spacer"></span>Fenwick Hollow, MD 20999</div>
  </div>
  <div class="contact contact--left-icons" style="left:187px;top:139px;">
    <div class="contact__line"><svg class="icon"><use href="#i-phone"/></svg>240.555.0143</div>
    <div class="contact__line"><svg class="icon"><use href="#i-fax"/></svg>240.555.0187</div>
    <div class="contact__line"><svg class="icon"><use href="#i-mail"/></svg>sales@verdantloopadvisors.example</div>
    <div class="contact__line"><svg class="icon"><use href="#i-web"/></svg>www.verdantloopadvisors.example</div>
  </div>
</section>
</body>
</html>
```